Business Card Design Project

We need business cards for the new company Market Helix based in Abu Dhabi, UAE, which provides IT retail solutions to businesses
Design should be done as a template, so we can add people when needed.
Please see attached details.
The brief is about 2 companies from our group. We need a business card only for Market Helix
Industry/Entity Type
Retail
Look and feel
Each slider illustrates characteristics of the customer's brand and the style your logo design should communicate.

```html
<!DOCTYPE html>
<html lang="en">
<head>
<meta charset="utf-8">
<title>Market Helix – Business Card</title>
<link rel="stylesheet" href="https://fonts.googleapis.com/css2?family=Source+Sans+3:wght@400;600;700&family=Noto+Naskh+Arabic:wght@400;700&display=swap">
<style>
  :root {
    --backdrop: #3a2f29;
    --card: #ffffff;
    --purple: #6a50a2;
    --gold: #d4ae3a;
    --gold-soft: #f0d67a;
    --panel-text: #f6e9b5;
  }
  * { margin: 0; padding: 0; box-sizing: border-box; }
  html, body { width: 1200px; height: 437px; overflow: hidden; }
  body {
    background: var(--backdrop);
    position: relative;
    font-family: "Source Sans 3", Arial, sans-serif;
  }
  .card {
    position: absolute;
    top: 84px;
    width: 485px;
    height: 276px;
    background: var(--card);
    overflow: hidden;
  }
  .card--front { left: 78px; }
  .card--back { left: 604px; }

  .brand {
    position: absolute;
    display: flex;
    align-items: center;
    gap: 8px;
    color: var(--purple);
    font-weight: 700;
    white-space: nowrap;
  }
  .brand__dot {
    width: 14px; height: 14px;
    border-radius: 50%;
    background: var(--gold);
    flex: none;
  }
  .card--front .brand { left: 36px; top: 118px; font-size: 30px; }
  .card--back .brand { left: 268px; top: 128px; font-size: 28px; }

  .company {
    position: absolute;
    left: 0; width: 245px;
    text-align: center;
    color: var(--purple);
  }
  .company__en { top: 216px; font-size: 14px; font-weight: 700; }
  .company__ar {
    top: 236px;
    font-family: "Noto Naskh Arabic", serif;
    font-size: 12px;
    font-weight: 700;
  }

  .divider {
    position: absolute;
    left: 247px; top: 0;
    width: 2px; height: 100%;
    background: var(--gold);
  }
  .panel {
    position: absolute;
    left: 249px; top: 0;
    width: 236px; height: 100%;
    background: var(--purple);
    padding: 0 0 0 22px;
    color: var(--panel-text);
  }
  .person__name-ar {
    position: absolute; top: 12px; left: 22px;
    font-family: "Noto Naskh Arabic", serif;
    font-size: 16px; font-weight: 700;
    color: var(--gold-soft);
  }
  .person__name {
    position: absolute; top: 40px; left: 22px;
    font-size: 15px; font-weight: 700;
    color: var(--gold-soft);
  }
  .person__title-ar {
    position: absolute; top: 68px; left: 22px;
    font-family: "Noto Naskh Arabic", serif;
    font-size: 11px;
  }
  .person__title {
    position: absolute; top: 91px; left: 22px;
    font-size: 11px;
  }
  .contact {
    position: absolute; top: 171px; left: 22px;
    list-style: none;
    font-size: 11px;
    line-height: 16.5px;
  }
  .contact__address { margin-bottom: 10px; }
  .contact b { font-weight: 700; }
</style>
</head>
<body>
  <section class="card card--front" aria-label="Business card front">
    <div class="brand"><span class="brand__dot"></span>Market Helix</div>
    <p class="company company__en">Gulf Provisions Co. L.L.C</p>
    <p class="company company__ar" dir="rtl">شركة الخليج للتموين المحدودة ذ م م</p>

    <div class="divider"></div>

    <div class="panel">
      <p class="person__name-ar" dir="rtl">كريم حداد</p>
      <p class="person__name">Karim Haddad</p>
      <p class="person__title-ar" dir="rtl">مدير حلول البيع بالتجزئة</p>
      <p class="person__title">Retail Solutions Manager</p>
      <ul class="contact">
        <li class="contact__address">PO Box - 50318, Abu Dhabi, UAE</li>
        <li><b>T :</b> +971 2 555 0142 - Ext: 210</li>
        <li><b>M:</b> +971 55 0107 386 ,</li>
        <li><b>F :</b> +971 2 555 0143</li>
        <li><b>E :</b> k.haddad@gulfprov.ae</li>
      </ul>
    </div>
  </section>

  <section class="card card--back" aria-label="Business card back">
    <div class="brand"><span class="brand__dot"></span>Market Helix</div>
  </section>
</body>
</html>
```